Business Card- Can you make it cool vs boring!

Need a refresh on my business card! Want it to be modern but simple, classic and a pop of coolness! we do senior living and it is boring. but that doesn't mean our business card have to look boring! Open to two sided cards. our website is www.Bruvel-HQ.com

Target Market(s)

capital market

Industry/Entity Type

senior housing/ real estate

Contact Information for Business Card

logo/ name/ cell/ address/ www.Bruvel-HQ.com/ space for a QR code

Requirements
Must have
• maybe a QR code (do not make prominent I may not use the QR so design where it can be taken out) that link to more about us/ landing page. needs to be modern but clean
Should not have
• clip art or script

```html
<!DOCTYPE html>
<html lang="en">
<head>
<meta charset="utf-8">
<title>Bruvel Living – Business Card</title>
<link href="https://fonts.googleapis.com/css2?family=Poppins:wght@400;500;700&display=swap" rel="stylesheet">
<style>
  :root {
    --backdrop: #5f2a13;
    --blush: #eed5cf;
    --paper: #ffffff;
    --rust: #b5532a;
    --ink: #222222;
    --dot-grey: #d6d6d6;
  }
  * { margin: 0; padding: 0; box-sizing: border-box; }
  html, body { width: 960px; height: 1200px; overflow: hidden; }
  body {
    background: var(--backdrop);
    font-family: "Poppins", sans-serif;
    position: relative;
  }
  .card {
    position: absolute;
    left: 49px;
    width: 863px;
    height: 493px;
    background: var(--paper);
    overflow: hidden;
  }
  .card--front { top: 73px; }
  .card--back { top: 626px; background: var(--blush); }
  .card__shapes { position: absolute; inset: 0; }
  .brand-name {
    position: absolute;
    font-weight: 500;
    color: var(--rust);
    white-space: nowrap;
    line-height: 1;
  }
  .card--front .brand-name {
    left: 0; width: 860px; text-align: center;
    top: 222px; font-size: 50px;
  }
  .card--back .brand-name {
    left: 57px; top: 62px; font-size: 34px;
  }
  .front-web {
    position: absolute;
    right: 55px; top: 432px;
    font-size: 22px; letter-spacing: 1.2px;
    color: var(--ink);
    line-height: 1;
  }
  .holder {
    position: absolute;
    right: 86px; top: 150px;
    text-align: right;
  }
  .holder__name {
    font-size: 42px; font-weight: 700; color: var(--rust);
    line-height: 1; letter-spacing: 0.5px;
  }
  .holder__title {
    font-size: 22px; letter-spacing: 4px; color: var(--ink);
    margin-top: 8px; margin-right: -4px; line-height: 1;
  }
  .contact {
    position: absolute;
    right: 122px;
    text-align: right;
    font-size: 22px; color: var(--ink);
    line-height: 29px; letter-spacing: 0.4px;
  }
  .contact--phone { top: 265px; }
  .contact--address { top: 310px; }
  .contact--web { top: 382px; letter-spacing: 1px; }
  .contact-icon {
    position: absolute; right: 80px;
    width: 32px; height: 32px;
  }
  .contact-icon--phone { top: 263px; }
  .contact-icon--pin { top: 321px; }
  .contact-icon--web { top: 380px; }
</style>
</head>
<body>

<section class="card card--front">
  <svg class="card__shapes" viewBox="0 0 863 493" width="863" height="493">
    <path d="M0 0 H463 C400 100 338 250 352 344 C366 440 450 478 550 452 L566 493 H0 Z" fill="var(--blush)"/>
  </svg>
  <div class="brand-name">Bruvel Living</div>
  <div class="front-web">www.bruvel-hq.com</div>
</section>

<section class="card card--back">
  <svg class="card__shapes" viewBox="0 0 863 493" width="863" height="493">
    <defs>
      <radialGradient id="halftone-fade" cx="0.05" cy="1" r="0.75">
        <stop offset="0" stop-color="#e6e6e6"/>
        <stop offset="0.6" stop-color="#f6f6f6"/>
        <stop offset="1" stop-color="#ffffff"/>
      </radialGradient>
    </defs>
    <path d="M0 493 C150 230 420 88 863 78 V493 Z" fill="var(--paper)"/>
    <path d="M0 493 C150 230 420 88 863 78 V493 Z" fill="url(#halftone-fade)" role="img" aria-label="Soft grey halftone dot pattern fading across the white area"/>
  </svg>

  <div class="brand-name">Bruvel Living</div>

  <div class="holder">
    <div class="holder__name">Dana Whitfield</div>
    <div class="holder__title">Senior</div>
  </div>

  <div class="contact contact--phone">(281) 555-0147</div>
  <svg class="contact-icon contact-icon--phone" viewBox="0 0 32 32">
    <circle cx="16" cy="16" r="16" fill="var(--rust)"/>
    <path d="M11.5 8.5 l3 3 -1.8 2.2 c1 2 2.6 3.6 4.6 4.6 l2.2-1.8 3 3 -1.6 2.6 c-6 -0.4 -11.6 -6 -12 -12 z" fill="#fff"/>
  </svg>

  <div class="contact contact--address">4870 Cedar Hollow Drive, Suite #1204<br>Maple Ridge, TX 77412</div>
  <svg class="contact-icon contact-icon--pin" viewBox="0 0 32 32">
    <circle cx="16" cy="16" r="16" fill="var(--rust)"/>
    <path d="M16 7 a6.5 6.5 0 0 1 6.5 6.5 c0 4.5 -6.5 11.5 -6.5 11.5 s-6.5 -7 -6.5 -11.5 A6.5 6.5 0 0 1 16 7 z" fill="#fff"/>
    <circle cx="16" cy="13.5" r="2.4" fill="var(--rust)"/>
  </svg>

  <div class="contact contact--web">www.bruvel-hq.com</div>
  <svg class="contact-icon contact-icon--web" viewBox="0 0 32 32">
    <circle cx="16" cy="16" r="16" fill="var(--rust)"/>
    <g fill="none" stroke="#fff" stroke-width="1.5">
      <circle cx="16" cy="16" r="8.5"/>
      <ellipse cx="16" cy="16" rx="3.8" ry="8.5"/>
      <line x1="7.5" y1="16" x2="24.5" y2="16"/>
      <line x1="9" y1="11.5" x2="23" y2="11.5"/>
      <line x1="9" y1="20.5" x2="23" y2="20.5"/>
    </g>
  </svg>
</section>

</body>
</html>
```